HIghly Competitive Dance School needs a web page make-over!!

Looking for a web design that captures our brand identity (Royal theme) that is New & Innovative and appeals to parents & children. I am open to creativity and want something original. Our color scheme is Burgundy & Gold with Black highlights. I currently use NetHarbor and have up to 10 pages to publish.
Updates

Reason: I have run into some problems that have prevented me from making a selection; please bear with me.

Reason: To all the designers...I apologize for the delay but I am in the middle of fall registration and construction on a new building. I can return to this task on Monday but I am deep in the middle of back-to-school. Please forgive me for this very long delay. Thanks for your understanding!!

To all the designers...I apologize for the delay but I am in the middle of fall registration and construction on a new building. I can return to this task on Monday but I am deep in the middle of back-to-school. Please forgive me for this very long delay. Thanks for your understanding!!

Target Market(s)

Parents with young children who have a disposable income

Industry/Entity Type

School

Requirements
Must have
• Home Page
Classes
Policies/Guidelines
Our Staff (with pictures)
Contact Us (complete your info here)
Our Story (history page)
Gallery (pictures & Videos)
Registration Form (with coinlark feature)

```html
<!DOCTYPE html>
<html lang="en">
<head>
<meta charset="utf-8">
<title>Heritage Dance Studio</title>
<link rel="stylesheet" href="https://fonts.googleapis.com/css2?family=Open+Sans:wght@400;600&family=Electrolize&display=swap">
<style>
:root{
  --burgundy:#6e0a26;
  --burgundy-dark:#4e0719;
  --red:#c4102a;
  --gold:#f0a93a;
  --gold-soft:#e7c47a;
  --ink:#141414;
  --bar:#1e1d1e;
  --grey:#555;
  --white:#fff;
  --muted:#8a8a8a;
}
*{box-sizing:border-box;margin:0;padding:0}
html,body{width:1200px;height:686px;overflow:hidden;background:var(--ink)}
.page{position:relative;width:1200px;height:686px;font-family:"Open Sans",sans-serif;color:var(--white)}

.sidebar{position:absolute;left:0;top:0;width:170px;height:686px;background:linear-gradient(180deg,var(--burgundy) 0%,var(--burgundy-dark) 100%)}
.brand{position:relative;height:132px;background:linear-gradient(180deg,#5a5a5a,#454545);display:flex;flex-direction:column;align-items:center;justify-content:center;gap:2px;color:var(--gold-soft);font-weight:600}
.brand::after{content:"";position:absolute;left:76px;bottom:-10px;border:10px solid transparent;border-bottom:0;border-top-color:#454545}
.brand-mark{width:18px;height:18px;background:var(--gold-soft);margin-bottom:6px}
.brand-name{font-size:26px;letter-spacing:.5px;line-height:1}
.brand-sub{font-size:9px;letter-spacing:.6px}

.nav{position:absolute;left:18px;top:180px;width:135px;list-style:none;font-family:"Electrolize",sans-serif;font-size:11.5px;letter-spacing:.5px;border-top:1px dotted var(--gold)}
.nav li{height:31.3px;line-height:31px;border-bottom:1px dotted var(--gold);color:var(--gold)}
.nav li.active{padding-left:15px}

.submenu{position:absolute;left:170px;top:304px;width:174px;list-style:none;font-family:"Electrolize",sans-serif;font-size:11px;letter-spacing:.8px}
.submenu li{height:31.3px;line-height:31px;padding-left:12px;background:#111;color:#9a9a9a}
.submenu li.current{background:var(--burgundy);color:var(--white)}

.call{position:absolute;left:14px;top:478px;line-height:1.1}
.call-label{font-size:18px}
.call-number{font-size:22px;font-weight:600}
.social{position:absolute;left:18px;top:569px;display:flex;gap:12px}
.social span{width:24px;height:24px;border-radius:50%;background:#a98a92;opacity:.8}
.copyright{position:absolute;left:18px;top:602px;font-size:10.5px;line-height:1.35}

.topbar{position:absolute;left:170px;top:0;width:1030px;height:56px;background:var(--bar);border-bottom:1px dotted #777}
.search{position:absolute;left:72px;top:11px;height:32px;padding-left:16px;border-left:1px dotted #777;line-height:32px;font-size:11px;color:var(--gold)}
.search-btn{position:absolute;right:0;top:0;width:55px;height:56px;background:#4a4a4a;display:flex;align-items:center;justify-content:center}

.hero{position:absolute;left:170px;top:57px;width:1030px;height:571px;background:radial-gradient(ellipse at 72% 45%,#7a6447 0%,#3b2f24 30%,#100d0c 62%),radial-gradient(ellipse at 10% 40%,#5a3a3a 0%,transparent 50%);background-blend-mode:screen}
.headline{position:absolute;left:240px;top:432px;height:58px;padding:0 8px;background:linear-gradient(90deg,#a80c22,var(--red));font-size:29px;line-height:58px;letter-spacing:.3px}
.subline{position:absolute;left:240px;top:498px;height:45px;padding:0 8px;background:rgba(30,30,30,.85);font-size:21px;line-height:45px;font-weight:400}

.player{position:absolute;left:170px;top:628px;width:1030px;height:58px;background:var(--bar);border-top:1px dotted var(--gold)}
.thumb{position:absolute;left:70px;top:9px;width:48px;height:44px;background:linear-gradient(135deg,#555,#222)}
.track{position:absolute;left:125px;top:10px}
.track-title{font-size:11px;font-weight:600;color:#bbb}
.track-share{margin-top:6px;font-size:8.5px;color:#888}
.track-share span+span{margin-left:8px;text-decoration:underline}
.controls{position:absolute;left:322px;top:12px}
.progress{position:absolute;left:404px;top:27px;width:160px;height:7px;background:#111;border:1px solid #333}
.progress i{display:block;width:44%;height:100%;background:var(--gold)}
.times{position:absolute;left:404px;top:38px;width:160px;display:flex;justify-content:space-between;font-size:8.5px;color:var(--muted)}
.volume{position:absolute;left:575px;top:27px;width:46px;height:7px;background:var(--gold)}
.shuffle-btn{position:absolute;left:916px;top:0;width:56px;height:58px;background:#4a4a4a;display:flex;align-items:center;justify-content:center}
.menu-btn{position:absolute;left:975px;top:0;width:55px;height:58px;background:var(--burgundy);display:flex;align-items:center;justify-content:center}
</style>
</head>
<body>
<div class="page">
  <aside class="sidebar">
    <div class="brand">
      <span class="brand-mark"></span>
      <span class="brand-name">HERITAGE</span>
      <span class="brand-sub">DANCE STUDIO, LLC</span>
    </div>
    <ul class="nav">
      <li>HOME</li><li>CLASSES</li><li>GUIDELINES</li><li>OUR STAFF</li>
      <li class="active">GALLERY</li><li>CONTACT</li><li>VIDEO</li><li>REGISTRATION</li>
    </ul>
    <div class="call"><div class="call-label">Call Us !</div><div class="call-number">555-014-7731</div></div>
    <div class="social"><span></span><span></span><span></span><span></span></div>
    <p class="copyright">Copyright © Heritage Dance<br>Studio,LLC 2013</p>
  </aside>

  <header class="topbar">
    <div class="search">Search...</div>
    <div class="search-btn">
      <svg width="30" height="30" viewBox="0 0 30 30"><circle cx="12" cy="12" r="8.5" fill="none" stroke="#fff" stroke-width="3.5"/><line x1="18.5" y1="18.5" x2="27" y2="27" stroke="#fff" stroke-width="4.5" stroke-linecap="round"/></svg>
    </div>
  </header>

  <section class="hero" role="img" aria-label="Sepia photograph of two ballet dancers in a lift against a dark background with soft light circles"></section>

  <ul class="submenu">
    <li>GALLERY COLUMN 1</li><li class="current">GALLERY COLUMN 1</li><li>GALLERY COLUMN 1</li>
  </ul>

  <h1 class="headline">"BUILDING GENERATIONS OF DANCERS..."</h1>
  <h2 class="subline">LOREM IPSUM DOLOR SIT AMET CONSECTEUR ADISCIPING</h2>

  <footer class="player">
    <div class="thumb" role="img" aria-label="Album cover showing dancers"></div>
    <div class="track">
      <div class="track-title">Veloren-Adagio In Gold</div>
      <div class="track-share"><span>Share on Circlo</span><span>Share on Chirpline</span></div>
    </div>
    <svg class="controls" width="72" height="34" viewBox="0 0 72 34">
      <circle cx="12" cy="17" r="11" fill="#f0a93a"/><circle cx="60" cy="17" r="11" fill="#f0a93a"/>
      <circle cx="36" cy="17" r="16" fill="#f0a93a"/>
      <path d="M7 17l5-4v8zM12 17l5-4v8z" fill="#4a2a00"/><path d="M65 17l-5-4v8zM60 17l-5-4v8z" fill="#4a2a00"/>
      <rect x="32" y="9" width="2.5" height="16" fill="#4a2a00"/><rect x="37.5" y="9" width="2.5" height="16" fill="#4a2a00"/>
    </svg>
    <div class="progress"><i></i></div>
    <div class="times"><span>00.02.53</span><span>00.05.54</span></div>
    <div class="volume"></div>
    <div class="shuffle-btn">
      <svg width="34" height="24" viewBox="0 0 34 24" fill="none" stroke="#fff" stroke-width="3"><path d="M2 5h7c6 0 10 14 16 14h5M2 19h7c6 0 10-14 16-14h5"/><path d="M27 1l4 4-4 4M27 15l4 4-4 4" stroke-width="2.5"/></svg>
    </div>
    <div class="menu-btn">
      <svg width="32" height="24" viewBox="0 0 32 24"><rect y="1" width="32" height="4" fill="#f0a93a"/><rect y="10" width="32" height="4" fill="#f0a93a"/><rect y="19" width="32" height="4" fill="#f0a93a"/></svg>
    </div>
  </footer>
</div>
</body>
</html>
```